Need an event poster for an automotive event.
The event is a half mile trap speed event. Sometimes called a VelMark event, they have a 1/2 mile to see how fast They can go. They run one car at a time, it is not a side-by-side race.
Title of the event is “KRBO Sidevalve Autumn Classic”. Dates are October 3-4 2020. Location Blytheville Arkansas. Website is KRBOmile.com. Most participants will be 50 and older .
All entries must be a carbureted flathead engine .

```html
<!DOCTYPE html>
<html lang="en">
<head>
<meta charset="utf-8">
<title>KRBO Sidevalve Autumn Classic</title>
<link rel="stylesheet" href="https://fonts.googleapis.com/css2?family=Montserrat:wght@600;700;800&display=swap">
<style>
  :root {
    --red: #ee3f22;
    --blue: #4a5db2;
    --navy: #34438a;
    --ink: #1e1d22;
    --grey-text: #47474d;
    --paper: #ffffff;
    --paper-soft: #efeff0;
  }
  * { margin: 0; padding: 0; box-sizing: border-box; }
  html, body { width: 1200px; height: 882px; overflow: hidden; background: var(--paper); }
  .poster {
    position: relative; width: 1200px; height: 882px; overflow: hidden;
    background: linear-gradient(90deg, var(--paper-soft) 0%, var(--paper) 60%);
    font-family: "Montserrat", Arial, sans-serif;
  }
  .stripes { position: absolute; inset: 0; }
  .brand {
    position: absolute; left: 420px; top: 140px;
    font-size: 62px; font-weight: 600; color: var(--grey-text); line-height: 1;
  }
  .title {
    position: absolute; left: 631px; top: 80px;
    color: var(--red); font-weight: 800; font-size: 50px; line-height: 1.2;
    letter-spacing: -0.5px; text-transform: uppercase;
  }
  .feature { position: absolute; left: 491px; width: 640px; height: 116px; }
  .feature--trophies { top: 229px; }
  .feature--certs { top: 351px; }
  .feature svg { position: absolute; inset: 0; }
  .feature__label {
    position: absolute; color: var(--paper); font-weight: 800; white-space: nowrap; text-transform: uppercase;
  }
  .feature--trophies .feature__label { left: 90px; top: 33px; font-size: 40px; }
  .feature--certs .feature__label { left: 110px; top: 42px; font-size: 24.5px; }
  .info { position: absolute; left: 595px; display: flex; align-items: center; gap: 22px; }
  .info--date { top: 484px; }
  .info--web { top: 545px; }
  .info__icon { flex: none; width: 51px; height: 51px; border-radius: 50%; background: var(--red); display: flex; align-items: center; justify-content: center; }
  .info__text { font-size: 26px; font-weight: 700; color: var(--grey-text); white-space: nowrap; }
  .info--web .info__text { font-size: 29px; }
  .car-photo {
    position: absolute; left: 0; top: 0; width: 1200px; height: 882px;
    background: radial-gradient(ellipse at 45% 75%, #ff3b4a 0%, #e0101e 55%, #8f0a12 100%);
    clip-path: polygon(73px 677px, 188px 571px, 269px 553px, 408px 555px, 571px 608px, 734px 645px, 783px 677px, 816px 735px, 808px 816px, 734px 865px, 490px 882px, 163px 824px, 73px 783px);
  }
  .badge {
    position: absolute; left: 755px; top: 621px; width: 228px; height: 228px; border-radius: 50%;
    background: var(--paper); border: 11px solid var(--red);
    display: flex; flex-direction: column; align-items: center; justify-content: center;
    font-weight: 800; line-height: 1.12; text-align: center;
  }
  .badge__distance { color: var(--red); font-size: 38px; }
  .badge__event { color: var(--grey-text); font-size: 38px; }
</style>
</head>
<body>
<main class="poster">
  <svg class="stripes" width="1200" height="882" viewBox="0 0 1200 882" aria-hidden="true">
    <polygon points="0,0 37,0 150,700 100,720 0,560" fill="var(--ink)"/>
    <polygon points="37,0 78,0 200,690 150,700" fill="var(--blue)"/>
    <polygon points="78,0 135,0 260,680 200,690" fill="var(--navy)"/>
    <polygon points="135,0 204,0 330,660 260,680" fill="var(--red)"/>
    <polygon points="204,0 261,0 375,640 330,660" fill="var(--ink)"/>
    <polygon points="261,0 318,0 420,620 375,640" fill="var(--blue)"/>
    <polygon points="0,720 120,740 560,882 0,882" fill="var(--navy)"/>
    <polygon points="120,740 560,740 1200,770 1200,845 560,882" fill="var(--blue)"/>
    <polygon points="600,882 1200,845 1200,882" fill="var(--ink)"/>
    <polygon points="60,800 420,800 640,882 30,882" fill="var(--red)"/>
  </svg>

  <div class="brand">KRBO</div>
  <h1 class="title">Sidevalve Autumn<br>Classic</h1>

  <div class="feature feature--trophies">
    <svg width="640" height="116" viewBox="0 0 640 116" aria-hidden="true">
      <defs><linearGradient id="shade1" x1="0" y1="0" x2="0" y2="1"><stop offset="0" stop-color="#000" stop-opacity=".18"/><stop offset="1" stop-color="#000" stop-opacity="0"/></linearGradient></defs>
      <polygon points="89,98 565,98 565,116 150,116" fill="url(#shade1)"/>
      <rect x="0" y="16" width="81" height="82" fill="var(--red)"/>
      <polyline points="18,58 34,74 64,40" fill="none" stroke="#fff" stroke-width="10" stroke-linecap="square"/>
      <polygon points="89,16 566,16 566,0 638,57 566,112 566,98 89,98" fill="var(--blue)"/>
    </svg>
    <span class="feature__label">Trophies Awards</span>
  </div>

  <div class="feature feature--certs">
    <svg width="640" height="116" viewBox="0 0 640 116" aria-hidden="true">
      <defs><linearGradient id="shade2" x1="0" y1="0" x2="0" y2="1"><stop offset="0" stop-color="#000" stop-opacity=".18"/><stop offset="1" stop-color="#000" stop-opacity="0"/></linearGradient></defs>
      <polygon points="89,98 565,98 565,116 150,116" fill="url(#shade2)"/>
      <rect x="0" y="16" width="81" height="82" fill="var(--red)"/>
      <polyline points="18,58 34,74 64,40" fill="none" stroke="#fff" stroke-width="10" stroke-linecap="square"/>
      <polygon points="89,16 566,16 566,0 638,57 566,112 566,98 89,98" fill="var(--blue)"/>
    </svg>
    <span class="feature__label">Certified Speed Certificates</span>
  </div>

  <div class="info info--date">
    <span class="info__icon">
      <svg width="24" height="22" viewBox="0 0 24 22" aria-hidden="true"><path d="M12 1 1 11h3v10h6v-6h4v6h6V11h3z" fill="#fff"/></svg>
    </span>
    <span class="info__text">OCT. 3-4, 2020 | BLYTHEVILLE, AR</span>
  </div>
  <div class="info info--web">
    <span class="info__icon">
      <svg width="26" height="18" viewBox="0 0 26 18" aria-hidden="true"><rect x="1" y="1" width="24" height="16" fill="none" stroke="#fff" stroke-width="2"/><polyline points="1,1 13,10 25,1" fill="none" stroke="#fff" stroke-width="2"/></svg>
    </span>
    <span class="info__text">KRBOmile.com</span>
  </div>

  <div class="car-photo" role="img" aria-label="Photo of a red sports coupe angled toward the viewer"></div>

  <div class="badge">
    <span class="badge__distance">1/2 MILE</span>
    <span class="badge__event">SPEED<br>TRIALS</span>
  </div>
</main>
</body>
</html>
```